pop up booking component and calendar re-design

we have a calander view where a parent cant reserve a day
you can click on please redesign the calander / voucher and pop up.

the dropdowns in pop up can be buttons
the dots on the calander indicate if there is space or not

when booking a day you can select a voucher

we used MELO as inspiration, you are welcome to look at it as well.. screenshots attached

please ask questions if you have any

```html
<!DOCTYPE html>
<html lang="en">
<head>
<meta charset="utf-8">
<title>Booking calendar</title>
<link href="https://fonts.googleapis.com/css2?family=Lato:wght@400;700&display=swap" rel="stylesheet">
<style>
:root{
  --stage:#139fd6;--panel:#f5f5f5;--white:#fff;--cyan:#30b7e8;--slate:#545e66;
  --booked:#5b7fb0;--booked-next:#89a8d2;--dark:#444c55;--muted:#88969c;--light:#efefef;
  --green:#57ad37;--dot-green:#8cc63f;--teal:#17b399;--red:#d9221c;--ink:#333;--grey-dot:#777;
  --orange:#f7941d;--popup:#d6f0f9;--tab:#b9e3f4;--petrol:#11759b;
}
*{box-sizing:border-box;margin:0;padding:0}
html,body{width:1200px;height:440px;overflow:hidden}
body{background:var(--stage);font-family:'Lato',sans-serif;position:relative}
.screen{position:absolute;top:35.9px;width:1238px;height:789px;background:var(--panel);transform:scale(.4658);transform-origin:0 0}
.screen--month{left:12.6px}.screen--booking{left:611.6px}
.abs{position:absolute}
.topbar{left:70px;top:41px;width:810px;height:44px;background:var(--slate);color:#fff;font-weight:700;font-size:18px}
.topbar .month{position:absolute;left:0;top:0;width:172px;height:44px;background:var(--cyan);line-height:44px;text-align:center;letter-spacing:.5px}
.topbar .nav{position:absolute;right:12px;top:0;line-height:44px;display:flex;gap:10px;align-items:center}
.calendar{left:70px;top:93px;width:810px;height:580px;background:var(--white)}
.weekdays{display:grid;grid-template-columns:repeat(7,105px);column-gap:9px;padding-left:13px;height:50px;align-items:center;font-size:13px;font-weight:700;color:var(--ink);border-bottom:1px solid #e6e6e6}
.weekdays span{text-align:center}
.grid{position:absolute;left:13px;top:58px;display:grid;grid-template-columns:repeat(7,105px);grid-auto-rows:78px;column-gap:9px;row-gap:8.6px}
.cell{position:relative;color:#fff;font-size:11.5px;line-height:14.5px;padding:32px 0 0 7px}
.cell .num{position:absolute;right:8px;top:6px;font-size:16px;font-weight:700}
.cell .dot{position:absolute;left:9px;top:9px;width:13px;height:13px;border-radius:50%}
.booked{background:var(--booked)}.booked .dot{background:var(--cyan)}
.booked-next{background:var(--booked-next)}.booked-next .dot{background:#7ccff0}
.taken{background:var(--dark)}.taken .dot{background:var(--cyan)}
.weekend{background:var(--dark)}.weekend .num{color:#c9ced2;font-weight:400}
.weekend-next{background:var(--muted)}.weekend-next .num{color:#d9dee0;font-weight:400}
.closed{background:var(--light);color:var(--ink)}.closed .dot{background:var(--grey-dot)}.closed .num{color:#666;font-weight:400}
.open{background:var(--light);color:var(--green)}.open .dot{background:var(--dot-green)}.open .num{color:#666;font-weight:400}
.open.next .num{color:#aaa}
.week{background:var(--slate);padding:0;display:flex;align-items:center;justify-content:center;font-size:30px;font-weight:700}
.week.next{background:var(--muted)}
.today{background:#3cc3f0;color:#fff;padding:0 3px;right:5px!important}
.side{left:893px;width:263px}
.side-btn{height:33px;color:#fff;font-size:12px;font-weight:700;text-align:center;line-height:33px;text-transform:uppercase}
.side-btn.cyan{background:var(--cyan);top:41px}
.side-btn.green{background:var(--green);top:83px}
.badge-count{display:inline-block;width:15px;height:15px;border-radius:50%;background:#3b6b2a;font-size:10px;line-height:15px;margin-left:3px}
.voucher{background:var(--white);height:150px}
.voucher .photo{height:110px;background:linear-gradient(120deg,#6d4a36 0%,#c8a07a 35%,#9fb8cf 60%,#e0c9a8 100%);position:relative}
.voucher .deal{position:absolute;right:6px;top:6px;width:68px;height:68px;border-radius:50%;background:var(--orange);color:#fff;font-size:13px;font-weight:700;text-align:center;padding-top:22px;line-height:15px}
.voucher .caption{position:absolute;left:0;right:0;bottom:0;height:32px;background:rgba(30,30,30,.7);color:#fff;font-size:13.5px;font-weight:700;line-height:32px;padding:0 8px 0 10px;display:flex;justify-content:space-between}
.voucher .caption b{font-size:15px}
.voucher .buy{display:flex;align-items:center;height:40px;padding:0 7px 0 12px;font-size:14px;color:var(--ink)}
.voucher .buy s{color:#888;margin-right:18px}
.voucher .buy strong{font-weight:700;flex:1}
.voucher .buy span{background:var(--cyan);color:#fff;font-weight:700;font-size:12px;width:93px;height:28px;line-height:28px;text-align:center}
.actions{top:696px;height:39px;color:#fff;font-size:14px;font-weight:700;line-height:39px;text-align:center;width:140px}
.btn-teal{left:70px;background:var(--teal)}.btn-dark{left:224px;background:#454545}.btn-red{left:682px;background:var(--red)}
.refresh{left:862px;top:704px}
.scale-tag{left:1195px;top:759px;font-size:13px;color:var(--ink)}
.popup{left:72px;top:323px;width:798px;height:340px;background:var(--popup);box-shadow:0 2px 6px rgba(0,0,0,.2)}
.tab{top:20px;height:35px;line-height:38px;font-size:15px;text-align:center;color:#2a3a48}
.tab.active{left:17px;width:138px;background:var(--white)}
.tab.other{left:163px;width:142px;background:var(--tab)}
.sheet{left:17px;top:55px;width:766px;height:265px;background:var(--white)}
.label{font-size:13.5px;color:var(--ink)}
.label.link{color:#3b6aa0}
.select{top:79px;width:135px;height:34px;border:1px solid #ccc;font-size:13.5px;line-height:32px;padding-left:11px;color:var(--ink)}
.select i{position:absolute;right:12px;top:0;font-style:normal;font-size:10px;line-height:15px;padding-top:2px}
.choice{top:123px;width:75px;height:35px;border:1.5px solid #4ab3c9;font-size:15px;font-weight:700;color:var(--ink);text-align:center;line-height:33px}
.choice em{font-style:normal;display:inline-block;width:16px;height:16px;border-radius:50%;background:#333;color:#fff;font-size:11px;line-height:16px;margin-left:4px;vertical-align:1px}
.toggle{left:434px;top:57px;width:16px;height:10px;border-radius:5px;background:#333}
.toggle::after{content:"";position:absolute;right:1px;top:1px;width:8px;height:8px;border-radius:50%;background:#fff}
.summary{left:518px;top:23px;width:233px;height:170px;background:#f2f2f2;padding:0 15px;font-size:14px;color:var(--ink)}
.summary .row{display:flex;justify-content:space-between;align-items:center;height:56px;border-bottom:1px solid #ddd}
.summary .row:last-child{border:0;font-weight:700}
.summary .apply{background:var(--petrol);color:#fff;font-weight:700;padding:2px 9px}
.pop-cancel{left:-17px;top:178px;width:140px;height:39px;background:var(--red);color:#fff;font-weight:700;font-size:14px;text-align:center;line-height:39px}
.pop-confirm{left:612px;top:206px;width:139px;height:39px;background:var(--petrol);color:#fff;font-weight:700;font-size:14px;text-align:center;line-height:39px}
</style>
</head>
<body>

<section class="screen screen--month">
  <div class="abs topbar"><div class="month">OCTOBER 2019</div><div class="nav"><svg width="10" height="14" viewBox="0 0 10 14"><path d="M8 1 2 7l6 6" fill="none" stroke="#fff" stroke-width="2.5"/></svg>TODAY<svg width="10" height="14" viewBox="0 0 10 14"><path d="m2 1 6 6-6 6" fill="none" stroke="#fff" stroke-width="2.5"/></svg></div></div>
  <div class="abs calendar">
    <div class="weekdays"><span>SUN</span><span>MON</span><span>TUE</span><span>WED</span><span>THU</span><span>FRI</span><span>SUN</span></div>
    <div class="grid">
      <div class="cell week">29</div>
      <div class="cell booked"><i class="dot"></i><b class="num">30</b>RBW-3-Penguins<br>07:30 -18:30<br>98.23</div>
      <div class="cell booked"><i class="dot"></i><b class="num">01</b>RBW-3-Penguins<br>07:30 -18:30<br>98.23</div>
      <div class="cell booked"><i class="dot"></i><b class="num">02</b>RBW-3-Penguins<br>07:30 -18:30<br>98.23</div>
      <div class="cell closed"><i class="dot"></i><b class="num">03</b></div>
      <div class="cell closed"><i class="dot"></i><b class="num">04</b></div>
      <div class="cell weekend"><b class="num">05</b></div>

      <div class="cell week">06</div>
      <div class="cell booked"><i class="dot"></i><b class="num">07</b>RBW-3-Penguins<br>07:30 -18:30<br>98.23</div>
      <div class="cell booked"><i class="dot"></i><b class="num">08</b>RBW-3-Penguins<br>07:30 -18:30<br>98.23</div>
      <div class="cell booked"><i class="dot"></i><b class="num">09</b>RBW-3-Penguins<br>07:30 -18:30<br>98.23</div>
      <div class="cell closed"><i class="dot"></i><b class="num">10</b></div>
      <div class="cell closed"><i class="dot"></i><b class="num">11</b></div>
      <div class="cell weekend"><b class="num">12</b></div>

      <div class="cell week">13</div>
      <div class="cell booked"><i class="dot"></i><b class="num">14</b>RBW-3-Penguins<br>07:30 -18:30<br>98.23</div>
      <div class="cell booked"><i class="dot"></i><b class="num">15</b>RBW-3-Penguins<br>07:30 -18:30<br>98.23</div>
      <div class="cell booked"><i class="dot"></i><b class="num today">16</b>RBW-3-Penguins<br>07:30 -18:30<br>98.23</div>
      <div class="cell open"><i class="dot"></i><b class="num">17</b>Om/Oa left</div>
      <div class="cell open"><i class="dot"></i><b class="num">18</b>Om/Oa left</div>
      <div class="cell weekend"><b class="num">19</b></div>

      <div class="cell week">20</div>
      <div class="cell booked"><i class="dot"></i><b class="num">21</b>RBW-3-Penguins<br>07:30 -18:30<br>98.23</div>
      <div class="cell booked"><i class="dot"></i><b class="num">22</b>RBW-3-Penguins<br>07:30 -18:30<br>98.23</div>
      <div class="cell booked"><i class="dot"></i><b class="num">23</b>RBW-3-Penguins<br>07:30 -18:30<br>98.23</div>
      <div class="cell open"><i class="dot"></i><b class="num">24</b>Om/Oa left</div>
      <div class="cell open"><i class="dot"></i><b class="num">25</b>Om/Oa left</div>
      <div class="cell weekend"><b class="num">26</b></div>

      <div class="cell week">27</div>
      <div class="cell booked"><i class="dot"></i><b class="num">28</b>RBW-3-Penguins<br>07:30 -18:30<br>98.23</div>
      <div class="cell taken"><i class="dot"></i><b class="num">29</b></div>
      <div class="cell taken"><i class="dot"></i><b class="num">30</b></div>
      <div class="cell open"><i class="dot"></i><b class="num">31</b>Om/Oa left</div>
      <div class="cell open next"><i class="dot"></i><b class="num">01</b>Om/Oa left</div>
      <div class="cell weekend-next"><b class="num">02</b></div>

      <div class="cell week next">03</div>
      <div class="cell booked-next"><i class="dot"></i><b class="num">04</b>RBW-3-Penguins<br>07:30 -18:30<br>98.23</div>
      <div class="cell booked-next"><i class="dot"></i><b class="num">05</b>RBW-3-Penguins<br>07:30 -18:30<br>98.23</div>
      <div class="cell booked-next"><i class="dot"></i><b class="num">06</b>RBW-3-Penguins<br>07:30 -18:30<br>98.23</div>
      <div class="cell open"><i class="dot"></i><b class="num">07</b>Om/Oa left</div>
      <div class="cell open next"><i class="dot"></i><b class="num">08</b>Om/Oa left</div>
      <div class="cell weekend-next"><b class="num">09</b></div>
    </div>
  </div>
  <div class="abs side side-btn cyan">Vouchers/Promotions</div>
  <div class="abs side side-btn green">Purchase <span class="badge-count">2</span></div>
  <div class="abs side voucher" style="top:128px"><div class="photo" role="img" aria-label="Photo of children reading together in a classroom"><div class="deal">10 Hours<br>@ € 8.9</div><div class="caption">Valid till 15th Dec 2019<b>0/10</b></div></div><div class="buy"><s>€ 89.00</s><strong>€ 89.00</strong><span>PURCHASE</span></div></div>
  <div class="abs side voucher" style="top:298px"><div class="photo" role="img" aria-label="Photo of children reading together in a classroom"><div class="deal">10 Hours<br>@ € 8.9</div><div class="caption">Valid till 15th Dec 2019<b>0/10</b></div></div><div class="buy"><s>€ 89.00</s><strong>€ 89.00</strong><span>PURCHASE</span></div></div>
  <div class="abs actions btn-teal">NOT COMING</div>
  <div class="abs actions btn-dark">UNSELECT</div>
  <div class="abs actions btn-red">CANCEL</div>
  <svg class="abs refresh" width="22" height="22" viewBox="0 0 22 22"><path d="M18 9A7.5 7.5 0 0 0 4.5 7M4 13a7.5 7.5 0 0 0 13.5 2" fill="none" stroke="#888" stroke-width="2.5"/><path d="M3 2v6h6M19 20v-6h-6" fill="none" stroke="#888" stroke-width="2.5"/></svg>
  <div class="abs scale-tag">X10</div>
</section>

<section class="screen screen--booking">
  <div class="abs topbar"><div class="month">OCTOBER 2019</div><div class="nav"><svg width="10" height="14" viewBox="0 0 10 14"><path d="M8 1 2 7l6 6" fill="none" stroke="#fff" stroke-width="2.5"/></svg>TODAY<svg width="10" height="14" viewBox="0 0 10 14"><path d="m2 1 6 6-6 6" fill="none" stroke="#fff" stroke-width="2.5"/></svg></div></div>
  <div class="abs calendar">
    <div class="weekdays"><span>SUN</span><span>MON</span><span>TUE</span><span>WED</span><span>THU</span><span>FRI</span><span>SUN</span></div>
    <div class="grid">
      <div class="cell week">29</div>
      <div class="cell booked"><i class="dot"></i><b class="num">30</b>RBW-3-Penguins<br>07:30 -18:30<br>98.23</div>
      <div class="cell booked"><i class="dot"></i><b class="num">01</b>RBW-3-Penguins<br>07:30 -18:30<br>98.23</div>
      <div class="cell booked"><i class="dot"></i><b class="num">02</b>RBW-3-Penguins<br>07:30 -18:30<br>98.23</div>
      <div class="cell closed"><i class="dot"></i><b class="num">03</b></div>
      <div class="cell closed"><i class="dot"></i><b class="num">04</b></div>
      <div class="cell weekend"><b class="num">05</b></div>
      <div class="cell week">06</div>
      <div class="cell booked"><i class="dot"></i><b class="num">07</b>RBW-3-Penguins<br>07:30 -18:30<br>98.23</div>
      <div class="cell booked"><i class="dot"></i><b class="num">08</b>RBW-3-Penguins<br>07:30 -18:30<br>98.23</div>
      <div class="cell booked"><i class="dot"></i><b class="num">09</b>RBW-3-Penguins<br>07:30 -18:30<br>98.23</div>
      <div class="cell closed"><i class="dot"></i><b class="num">10</b></div>
      <div class="cell closed"><i class="dot"></i><b class="num">11</b></div>
      <div class="cell weekend"><b class="num">12</b></div>
    </div>
  </div>

  <div class="abs popup">
    <div class="abs tab active">BOOK DAY</div>
    <div class="abs tab other">VOUCHERS</div>
    <div class="abs sheet">
      <div class="abs label link" style="left:20px;top:21px">Availability-</div>
      <div class="abs label link" style="left:121px;top:21px">1m/1a left 24-10-2019</div>
      <div class="abs label" style="left:20px;top:53px">Locations*</div>
      <div class="abs label" style="left:179px;top:53px">Groups*</div>
      <div class="abs label" style="left:360px;top:53px">BSO</div>
      <div class="abs toggle"></div>
      <div class="abs select" style="left:20px">RBW<i>▲<br>▼</i></div>
      <div class="abs select" style="left:179px">3-Penguins<i>▲<br>▼</i></div>
      <div class="abs choice" style="left:20px">FULL<em>1</em></div>
      <div class="abs choice" style="left:105px">AM <em>1</em></div>
      <div class="abs choice" style="left:188px">PM <em>3</em></div>
      <div class="abs choice" style="left:271px">FLEX</div>
      <div class="abs choice" style="left:356px">TRY</div>
      <div class="abs pop-cancel" style="left:17px">CANCEL</div>
      <div class="abs summary">
        <div class="row"><span>PRICE</span><span>€ 98.23</span></div>
        <div class="row"><span>VOUCHER</span><span class="apply">Apply</span></div>
        <div class="row"><span>TOTAL</span><span>€ 98.23</span></div>
      </div>
      <div class="abs pop-confirm">CONFIRM</div>
    </div>
  </div>

  <div class="abs side side-btn cyan">Vouchers/Promotions</div>
  <div class="abs side side-btn green">Purchase <span class="badge-count">2</span></div>
  <div class="abs side voucher" style="top:128px"><div class="photo" role="img" aria-label="Photo of children reading together in a classroom"><div class="deal">10 Hours<br>@ € 8.9</div><div class="caption">Valid till 15th Dec 2019<b>0/10</b></div></div><div class="buy"><s>€ 89.00</s><strong>€ 89.00</strong><span>PURCHASE</span></div></div>
  <div class="abs side voucher" style="top:298px"><div class="photo" role="img" aria-label="Photo of children reading together in a classroom"><div class="deal">10 Hours<br>@ € 8.9</div><div class="caption">Valid till 15th Dec 2019<b>0/10</b></div></div><div class="buy"><s>€ 89.00</s><strong>€ 89.00</strong><span>PURCHASE</span></div></div>
  <div class="abs actions btn-teal">NOT COMING</div>
  <div class="abs actions btn-dark">UNSELECT</div>
  <div class="abs actions btn-red">CANCEL</div>
  <svg class="abs refresh" width="22" height="22" viewBox="0 0 22 22"><path d="M18 9A7.5 7.5 0 0 0 4.5 7M4 13a7.5 7.5 0 0 0 13.5 2" fill="none" stroke="#888" stroke-width="2.5"/><path d="M3 2v6h6M19 20v-6h-6" fill="none" stroke="#888" stroke-width="2.5"/></svg>
  <div class="abs scale-tag">X10</div>
</section>

</body>
</html>
```